Packaging design for HOT NEW RETAIL BEARD OIL BRAND - Merrow Fennick Apothecary

Packaging design for beard oils. I've attached a brief, and I've also attached a few examples of bottles and boxes. Of course, we need an entirely unique look. I've attached the photo of Merrow Fennick as well - you can choose to use it or not (I'm open).

This product will be sold at national retailers and needs to look like a brand that is sold at boutique

What the consumer wants to see on the shelf:
-Box should larger than others and be soft touch (feels luxurious)
-More “hipster look/feel”
-Text should stand out like inspiration photos - jumping off the shelf to the consumer
-Use the existing logo of Merrow Fennick
-Deco will be wrap label as shown in current product image
-Sample text to pull copy for outer carton (taken from label on glass bottle):
-Strengthen and condition your beard with this blend of natural oils. Sunflower oil is rich in omega, fatty acids and vitamins E, C, B, and A, while avocado oil hydrates the beard fibers from root to tip, keep the beard looking and feeling extraordinary. Smooth into your beard for a healthy sheen and a woodsy scent evoking the great outdoors.
-Cool/Hipster product at discount pricing

Target Market(s)

Men from ages 20-40. Women also buy this product for their men, so it needs to look like a well known brand.

Industry/Entity Type

Hair And Beauty

Font styles to use
Sans Serif

Colors

Designer to choose colors to be used in the design.

Requirements
Must have
• A full label and box design with key call outs:
• Features and benefits - found in attached brief
• Description of what it is: Beard Oil
• Name of frangrance: Sandalwood
• Size: 2 oz / 60 ml
Nice to have
• Feel free to revamp the logo if needed. I am not married to the font for Merrow Fennick Apothecary.

```html
<!DOCTYPE html>
<html lang="en">
<head>
<meta charset="utf-8">
<title>Merrow Fennick Apothecary — Softening Beard Oil Cartons</title>
<link rel="stylesheet" href="https://fonts.googleapis.com/css2?family=Bebas+Neue&family=Cormorant+Garamond:wght@500&family=Raleway:wght@300&display=swap">
<style>
  :root {
    --backdrop: #e2e2e2;
    --carton: #111111;
    --ink-light: #f1efea;
    --paper: #e9e6df;
    --ink-dark: #141414;
    --rule: #d8d6d0;
    --muted: #8d8d8d;
    --cool-breeze: #4b7380;
    --wood-reserve: #a2892a;
    --lavender-citrus: #d4d2cd;
  }
  * { margin: 0; padding: 0; box-sizing: border-box; }
  html, body { width: 1200px; height: 900px; overflow: hidden; background: var(--backdrop); }
  .stage { position: relative; width: 1200px; height: 900px; }

  .carton {
    position: absolute; top: 278px; width: 244px; height: 373px;
    background: var(--carton); color: var(--ink-light);
    font-family: "Bebas Neue", sans-serif; text-align: center;
  }
  .carton--cool { left: 108px; --flavour: var(--cool-breeze); --flavour-ink: var(--ink-light); }
  .carton--wood { left: 480px; --flavour: var(--wood-reserve); --flavour-ink: var(--ink-light); }
  .carton--lavender { left: 841px; --flavour: var(--lavender-citrus); --flavour-ink: var(--ink-dark); }

  .frame { position: absolute; left: 30px; top: 46px; width: 183px; height: 302px; border: 1px solid var(--rule); }
  .frame-dashed { position: absolute; left: 38px; top: 53px; width: 167px; height: 287px; border: 1px dashed #7a7a7a; }

  .brand-seal {
    position: absolute; left: 81px; top: 3px; width: 82px; height: 82px; border-radius: 50%;
    background: var(--carton); border: 1px solid var(--ink-light); box-shadow: 0 0 0 6px var(--carton);
    display: flex; align-items: center; justify-content: center;
    font-size: 13px; line-height: 1.05; letter-spacing: .5px;
  }

  .line { position: absolute; left: 0; width: 100%; white-space: nowrap; line-height: 1; }
  .brand-name { top: 91px; font-size: 20px; }
  .brand-sub { top: 113px; font-size: 13px; }

  .title-band { position: absolute; left: 30px; top: 133px; width: 183px; height: 65px; background: var(--paper); }
  .title-box { position: absolute; left: 8px; top: 8px; width: 167px; height: 47px; border: 1px solid var(--ink-dark); }
  .title-tag {
    position: absolute; left: 50%; top: -7px; transform: translateX(-50%);
    background: var(--carton); color: var(--ink-light); padding: 0 3px;
    font-family: "Cormorant Garamond", serif; font-weight: 500; font-size: 12px; line-height: 13px; letter-spacing: .5px;
  }
  .title-main { position: absolute; left: 0; top: 10px; width: 100%; font-size: 36px; line-height: 1; color: var(--ink-dark); }

  .benefit-head { top: 204px; font-size: 13.5px; }
  .benefit-sub { top: 223px; font-size: 8.5px; }
  .divider { position: absolute; left: 76px; top: 239px; width: 92px; height: 1px; background: var(--rule); }
  .ingredients { top: 246px; font-size: 11.5px; }
  .vitamins { top: 260px; font-size: 14.5px; }
  .tagline { top: 281px; font-size: 13px; }
  .tagline::before, .tagline::after { content: "•"; margin: 0 5px; font-size: 10px; vertical-align: 2px; }

  .scent-band {
    position: absolute; left: 38px; top: 304px; width: 167px; height: 29px;
    background: var(--flavour); color: var(--flavour-ink);
    font-size: 21px; line-height: 31px;
  }
  .volume { top: 356px; font-family: "Raleway", sans-serif; font-weight: 300; font-size: 8px; color: var(--muted); }
</style>
</head>
<body>
<main class="stage">

  <article class="carton carton--cool">
    <div class="frame"></div><div class="frame-dashed"></div>
    <div class="brand-seal">MERROW<br>FENNICK</div>
    <p class="line brand-name">MERROW FENNICK</p>
    <p class="line brand-sub">APOTHECARY</p>
    <div class="title-band"><div class="title-box"><span class="title-tag">SOFTENING</span><h2 class="title-main">BEARD OIL</h2></div></div>
    <p class="line benefit-head">STRENGTHEN AND CONDITION</p>
    <p class="line benefit-sub">YOUR BEARD WITH THIS BLEND OF NATURAL OILS</p>
    <div class="divider"></div>
    <p class="line ingredients">SUNFLOWER OIL &amp; AVOCADO OIL</p>
    <p class="line vitamins">VITAMINS E, C, B, AND A</p>
    <p class="line tagline">BEST OIL FOR GENTLEMEN</p>
    <p class="scent-band">COOL BREEZE</p>
    <p class="line volume">60 ml / 2 fl oz</p>
  </article>

  <article class="carton carton--wood">
    <div class="frame"></div><div class="frame-dashed"></div>
    <div class="brand-seal">MERROW<br>FENNICK</div>
    <p class="line brand-name">MERROW FENNICK</p>
    <p class="line brand-sub">APOTHECARY</p>
    <div class="title-band"><div class="title-box"><span class="title-tag">SOFTENING</span><h2 class="title-main">BEARD OIL</h2></div></div>
    <p class="line benefit-head">STRENGTHEN AND CONDITION</p>
    <p class="line benefit-sub">YOUR BEARD WITH THIS BLEND OF NATURAL OILS</p>
    <div class="divider"></div>
    <p class="line ingredients">SUNFLOWER OIL &amp; AVOCADO OIL</p>
    <p class="line vitamins">VITAMINS E, C, B, AND A</p>
    <p class="line tagline">BEST OIL FOR GENTLEMEN</p>
    <p class="scent-band">WOOD RESERVE</p>
    <p class="line volume">60 ml / 2 fl oz</p>
  </article>

  <article class="carton carton--lavender">
    <div class="frame"></div><div class="frame-dashed"></div>
    <div class="brand-seal">MERROW<br>FENNICK</div>
    <p class="line brand-name">MERROW FENNICK</p>
    <p class="line brand-sub">APOTHECARY</p>
    <div class="title-band"><div class="title-box"><span class="title-tag">SOFTENING</span><h2 class="title-main">BEARD OIL</h2></div></div>
    <p class="line benefit-head">STRENGTHEN AND CONDITION</p>
    <p class="line benefit-sub">YOUR BEARD WITH THIS BLEND OF NATURAL OILS</p>
    <div class="divider"></div>
    <p class="line ingredients">SUNFLOWER OIL &amp; AVOCADO OIL</p>
    <p class="line vitamins">VITAMINS E, C, B, AND A</p>
    <p class="line tagline">BEST OIL FOR GENTLEMEN</p>
    <p class="scent-band">LAVENDER CITRUS</p>
    <p class="line volume">60 ml / 2 fl oz</p>
  </article>

</main>
</body>
</html>
```